Vortelan d.o.o. needes a web site design

We are a company dealing with automatic doors, industrial doors, roller shutters, access control systems.
We would like to get a design which is clean and neat, and here are some sites which work with similar products. These designs are some we like, but of course, I am looking for a design which is unique. We usually use grey and red colours, which you can see on www.vortelan.ba .
The sites we like are:
http://www.plexawin.com/gb/
http://www.brunosteca.it/eng/
http://faswoodportamel.com/

You have to understand, that we have 4 different groups of products, which are main groups. I would like if those 4 groups somehow could be in different colours. (Maybe "zuvex" colours), in order to separate the groups in some way.

Attached you have web site structure.

If any questions, please contact me.
Edvin

Target Market(s)

Bosnian market. Aluminium and PVC doors and window market, Construction companies, Supermarkets-Retail, Gas stations, Banks, Food industry, Heavy industry.

Industry/Entity Type

It Company

Contact Information for Business Card

I have attached our current business card in PDF. I weould like english on one side, bosnian on other side.

Logo Text

Vortelan is the name of the company, our core business is automation!

Number of Pages Required

5+ page

Font styles to use
Sans Serif

Colors
ec1f27
0792cd
9bcb3c
ffc214
ffffff

```html
<!DOCTYPE html>
<html lang="bs">
<head>
<meta charset="utf-8">
<title>Vortelan d.o.o.</title>
<link href="https://fonts.googleapis.com/css2?family=Lato:wght@400;700&family=Mulish:ital,wght@0,600;0,800;1,600;1,700;1,800&family=Oswald:wght@400;500&display=swap" rel="stylesheet">
<style>
:root{
  --red:#e52d35;
  --red-dark:#c81f27;
  --group-blue:#0792cd;
  --group-green:#9bcb3c;
  --group-yellow:#ffc214;
  --group-red:#ec1f27;
  --grey-dark:#3a3a3a;
  --grey-nav:#555656;
  --grey-mid:#6a6a6a;
  --grey-light:#efefef;
  --text:#555;
  --white:#fff;
}
*{box-sizing:border-box;margin:0;padding:0}
html,body{width:1200px;height:2490px;overflow:hidden}
body{font-family:"Lato",sans-serif;color:var(--text);background:var(--white);position:relative}
.abs{position:absolute}
.heading{font-family:"Mulish",sans-serif;font-style:italic;font-weight:700;color:var(--grey-dark)}
.heading .cap{color:var(--red)}
.divider{position:absolute;height:2px;background:#ddd}
.divider::after{content:"";position:absolute;left:50%;top:-5px;width:12px;height:12px;margin-left:-6px;background:var(--red);transform:rotate(45deg)}

/* header */
.site-header{left:0;top:0;width:1200px;height:103px;background:linear-gradient(#fff,#f2f2f2)}
.brand{left:52px;top:30px;display:flex;align-items:center;gap:10px;font-family:"Mulish",sans-serif;font-weight:800;font-size:38px;color:var(--red);letter-spacing:1px}
.brand-mark{width:20px;height:20px;background:var(--grey-mid)}
.brand small{font-size:18px}
.contact-top{right:52px;top:18px;font-size:15px;color:#444;display:flex;align-items:center;gap:10px}
.contact-top .sep{width:1px;height:18px;background:#ccc}
.social{display:flex;gap:4px}
.social span{width:20px;height:20px;background:#7a7a7a;display:block}
.call{right:52px;top:50px;font-size:25px;color:var(--red)}
.call strong{color:#333;font-weight:400}

/* nav */
.main-nav{left:0;top:103px;width:1200px;height:47px;background:var(--grey-nav)}
.main-nav a{position:absolute;top:14px;font-family:"Mulish",sans-serif;font-style:italic;font-weight:600;font-size:15px;color:#fff;text-decoration:none}
.main-nav .active{left:52px;top:0;width:76px;height:47px;background:var(--red);text-align:center;line-height:47px}
.redesign{left:935px;top:98px;width:215px;height:52px;background:var(--red);color:#fff;font-family:"Mulish",sans-serif;font-style:italic;font-weight:700;font-size:20px;text-align:center;line-height:52px;border-radius:3px 3px 0 0}

/* hero */
.hero{left:0;top:150px;width:1200px;height:467px}
.ph{position:absolute}
.hero-title{left:797px;top:140px;font-family:"Oswald",sans-serif;color:#fff;font-size:50px;font-weight:400;letter-spacing:1px}
.hero-sub{left:797px;top:202px;width:360px;font-family:"Oswald",sans-serif;color:#fff;font-size:14px;line-height:22px;text-align:center}
.dots{left:568px;top:436px;display:flex;gap:9px}
.dots span{width:12px;height:12px;border-radius:50%;background:#ddd}
.dots span:first-child{background:var(--red)}

/* welcome */
.welcome h1{left:0;top:660px;width:1200px;text-align:center;font-size:30px}
.welcome h1 .name{color:var(--red);font-weight:800;font-size:38px}
.welcome h1 small{font-size:17px;color:#555}
.lead{left:72px;width:1056px;text-align:center;font-size:14px;line-height:24px;color:#666}
.btn-red{background:var(--red);color:#fff;font-family:"Mulish",sans-serif;font-style:italic;font-weight:700;font-size:15px;text-align:center;border-radius:6px 0 6px 0;transform:skewX(-12deg)}
.btn-red span{display:block;transform:skewX(12deg)}
.band-shadow{left:0;top:912px;width:1200px;height:14px;background:linear-gradient(rgba(0,0,0,.08),rgba(0,0,0,0))}

/* product groups */
.tile{position:absolute;top:1090px;width:298px;height:263px;overflow:hidden;--group:var(--red)}
.tile.group-automatic{--group:var(--group-blue)}
.tile.group-industrial{--group:var(--group-green)}
.tile.group-shutters{--group:var(--group-yellow)}
.tile.group-access{--group:var(--group-red)}
.tile-label{position:absolute;left:0;bottom:0;width:100%;height:42px;background:var(--group);color:#fff;font-family:"Mulish",sans-serif;font-style:italic;font-weight:700;font-size:18px;text-align:center;line-height:42px}
.group-shutters .tile-label{color:#333}
.tile-hover{background:rgba(85,85,85,.93);color:#fff;padding:18px 22px;border-bottom:6px solid var(--group)}
.tile-hover h3{font-family:"Mulish",sans-serif;font-style:italic;font-weight:600;font-size:18px;margin-bottom:10px}
.tile-hover p{font-size:13px;line-height:21px;margin-bottom:10px}
.tile-hover li{list-style:none;font-size:13px;line-height:28px;padding-left:30px;position:relative}
.tile-hover li::before{content:"";position:absolute;left:4px;top:8px;width:7px;height:11px;border-right:3px solid var(--group);border-bottom:3px solid var(--group);transform:rotate(40deg)}
.view-all{position:absolute;left:28px;bottom:14px;width:100px;height:30px;background:#333;color:#fff;font-family:"Mulish",sans-serif;font-style:italic;font-weight:700;font-size:14px;line-height:30px;text-align:center;border-radius:14px 0 0 0;border-left:4px solid var(--group)}

/* partners */
.partners{left:0;top:1353px;width:1200px;height:216px;background:var(--grey-light)}
.partner{position:absolute;top:82px;font-family:"Mulish",sans-serif;font-weight:800;font-size:40px;color:#222}

/* inquiry */
.inquiry{left:0;top:1569px;width:1200px;height:211px;background:linear-gradient(#5a5a5a,#484848)}
.inquiry h2{position:absolute;left:0;top:34px;width:1200px;text-align:center;color:#fff;font-size:32px}
.field{position:absolute;top:133px;height:33px;background:#fff;border-radius:3px;font-size:13px;color:#444;padding:9px 10px}

/* columns */
.col-title{font-size:25px}
.why li{list-style:none;font-size:13px;line-height:19px;color:#444;padding:0 0 15px 30px;margin-bottom:14px;border-bottom:1px dotted #bbb;position:relative}
.why li::before{content:"+";position:absolute;left:4px;top:-3px;color:var(--red);font-size:22px;font-weight:700}
.news-item{position:absolute;left:425px;width:360px;height:68px}
.date{position:absolute;left:0;top:0;width:44px;height:52px;border:1px solid #ddd;text-align:center}
.date b{display:block;background:var(--red);color:#fff;font-size:20px;line-height:28px}
.date i{font-style:normal;font-size:12px;color:#444;line-height:22px}
.news-item h4{position:absolute;left:65px;top:-2px;font-size:14px;color:#333;font-weight:700}
.news-item p{position:absolute;left:65px;top:20px;width:270px;font-size:13px;line-height:19px;color:#555}

/* footer */
.footer{left:0;top:2130px;width:1200px;height:297px;background:linear-gradient(#3c3c3c,#222)}
.footer h3{font-family:"Mulish",sans-serif;font-style:italic;font-weight:700;font-size:18px;color:#fff}
.footer-text{font-size:13px;line-height:20px;color:#ddd}
.f-input{position:absolute;width:205px;height:32px;background:#111;border:1px solid #444;font-size:13px;color:#666;padding:8px 8px}
.links li{list-style:none;font-size:13px;color:#ddd;line-height:29px}
.links li::before{content:"›";margin-right:8px}
.bottom-bar{left:0;top:2427px;width:1200px;height:63px;background:#1a1a1a}
</style>
</head>
<body>

<header class="abs site-header">
  <div class="abs brand"><span class="brand-mark"></span>vortelan <small>d.o.o.</small></div>
  <div class="abs contact-top">
    <svg width="16" height="12" viewBox="0 0 16 12"><rect width="16" height="12" fill="#e52d35"/><path d="M0 0l8 7 8-7" fill="none" stroke="#fff" stroke-width="1.5"/></svg>
    info@vortelan.ba <span class="sep"></span> Follow Us:
    <span class="social" aria-label="Social links"><span></span><span></span><span></span></span>
  </div>
  <div class="abs call">CALL US TODAY : <strong>033/417-592</strong></div>
</header>

<nav class="abs main-nav">
  <a class="active" href="#">Home</a>
  <a style="left:178px" href="#">Industrijska Vrata</a>
  <a style="left:367px" href="#">Rolo Vrata</a>
  <a style="left:508px" href="#">Kontrola Pristupa</a>
  <a style="left:697px" href="#">Reference</a>
  <a style="left:838px" href="#">Contact</a>
</nav>
<div class="abs redesign">Redizajn Stranice</div>

<section class="abs hero">
  <div class="ph" role="img" aria-label="Woman answering an intercom handset" style="left:0;top:0;width:278px;height:313px;background:linear-gradient(135deg,#d9d6d3,#8a7a72)"></div>
  <div class="ph" role="img" aria-label="Woman pressing a video door phone" style="left:282px;top:0;width:249px;height:233px;background:linear-gradient(135deg,#c8c0b6,#6e6a72)"></div>
  <div class="ph" role="img" aria-label="Keypad close-up" style="left:0;top:317px;width:278px;height:150px;background:linear-gradient(135deg,#a09690,#4a3f3a)"></div>
  <div class="ph" role="img" aria-label="Woman speaking on an intercom beside a wall panel" style="left:282px;top:237px;width:249px;height:230px;background:linear-gradient(135deg,#9a9896,#3e3e3e)"></div>
  <div class="ph" role="img" aria-label="Finger pressing a wall-mounted access keypad" style="left:535px;top:0;width:665px;height:467px;background:linear-gradient(120deg,#5a5855,#9a958e 55%,#6c6864)"></div>
  <div class="abs hero-title">nova web stranica</div>
  <div class="abs hero-sub">u toku su radovi na novoj web prezentaciji naših usluga,<br>uskoro smo ponovo sa vama</div>
  <div class="abs dots"><span></span><span></span><span></span></div>
</section>

<section class="welcome">
  <h1 class="abs heading">Welcome to <span class="name">vortelan</span> <small>d.o.o.</small></h1>
  <div class="divider" style="left:498px;top:715px;width:204px"></div>
  <p class="abs lead" style="top:742px">Lorem ipsum dolor sit amet, consectetuer adipiscing elit, sed diam nonummy nibh euismod tincidunt ut laoreet dolore magna aliquam erat volutpat. Ut wisi enim ad minim veniam, quis nostrud exerci tation ullamcorper suscipit lobortis nisl ut aliquip ex ea commodo consequat. Duis autem vel eum iriure dolor in hendrerit in vulputate velit esse molestie consequat, vel illum dolore eu feugiat nulla facilisis at vero eros et accumsan et iusto Ut wisi enim ad minim veniam,</p>
  <div class="abs btn-red" style="left:542px;top:834px;width:118px;height:32px;line-height:32px"><span>Read More</span></div>
</section>
<div class="abs band-shadow"></div>

<section class="products">
  <h2 class="abs heading" style="left:0;top:958px;width:1200px;text-align:center;font-size:31px">We Are <span class="cap">C</span>ompany <span class="cap">D</span>ealing <span class="cap">W</span>ith</h2>
  <div class="divider" style="left:447px;top:1015px;width:306px"></div>
  <p class="abs lead" style="top:1050px">Lorem ipsum dolor sit amet, consectetuer adipiscing elit, sed diam nonummy nibh euismod tincidunt ut laoreet dolore</p>

  <div class="tile group-automatic" style="left:0">
    <div class="ph" role="img" aria-label="Glass automatic sliding doors at a building entrance" style="inset:0;background:linear-gradient(135deg,#e0e2e0,#8c9088)"></div>
    <div class="tile-label">Automatic Doors</div>
  </div>
  <div class="tile tile-hover group-industrial" style="left:302px">
    <h3>Industrial Doors</h3>
    <p>Lorem ipsum dolor sit amet, consectetuer adipiscing elit, sed diam nonummy</p>
    <ul><li>Lorem ipsum dolor sit amet</li><li>Lorem ipsum dolor sit amet</li><li>Lorem ipsum dolor sit amet</li></ul>
    <div class="view-all">View All</div>
  </div>
  <div class="tile group-shutters" style="left:602px">
    <div class="ph" role="img" aria-label="Row of closed roller shutters in a warehouse" style="inset:0;background:linear-gradient(135deg,#b8b8b6,#5c5c5a)"></div>
    <div class="tile-label">Roller Shutters</div>
  </div>
  <div class="tile group-access" style="left:902px">
    <div class="ph" role="img" aria-label="Woman swiping a card at an access reader" style="inset:0;background:linear-gradient(135deg,#c2a88c,#6c5a4a)"></div>
    <div class="tile-label">Access Control Systems</div>
  </div>
</section>

<section class="abs partners">
  <div class="partner" style="left:245px">Travexo</div>
  <div class="partner" style="left:520px">Norlida</div>
  <div class="partner" style="left:790px;display:flex;align-items:center;gap:10px"><span style="width:22px;height:22px;border-radius:50%;background:#555;display:block"></span>Orvanta</div>
</section>

<section class="abs inquiry">
  <h2 class="heading" style="color:#fff">Quick Inquiry</h2>
  <div class="divider" style="left:540px;top:86px;width:120px;background:#777"></div>
  <div class="field" style="left:50px;width:282px">Name</div>
  <div class="field" style="left:342px;width:280px">Email</div>
  <div class="field" style="left:632px;width:385px">Message</div>
  <div class="abs btn-red" style="left:1034px;top:133px;width:112px;height:33px;line-height:33px;font-size:17px"><span>Submit</span></div>
</section>

<section class="columns">
  <h3 class="abs heading col-title" style="left:52px;top:1815px"><span class="cap">W</span>hy <span class="cap">C</span>hoose <span class="cap">U</span>s</h3>
  <ul class="abs why" style="left:52px;top:1880px;width:285px">
    <li>Lorem ipsum dolor sit tetu adipiscing elised diam nonummy nibh euismod</li>
    <li>Lorem ipsum dolor sit tetu adipiscing elised diam nonummy nibh euismod</li>
    <li>Lorem ipsum dolor sit tetu adipiscing el.</li>
    <li style="border:none">Ktu adipiscing elitsied orem ipsum dolo.</li>
  </ul>

  <h3 class="abs heading col-title" style="left:425px;top:1815px"><span class="cap">L</span>atest <span class="cap">N</span>ews</h3>
  <svg class="abs" style="left:750px;top:1825px" width="40" height="16" viewBox="0 0 40 16"><path d="M10 2l-6 6 6 6M30 2l6 6-6 6" fill="none" stroke="#555" stroke-width="2.5"/></svg>
  <div class="news-item" style="top:1885px"><div class="date"><b>01</b><i>MAR</i></div><h4>Lorem ipsum dolor sitak ametn sit almet</h4><p>Lorem ipsum dolor sitak amet, co adipiscing elit, euismod poor.</p></div>
  <div class="news-item" style="top:1957px"><div class="date"><b>03</b><i>MAR</i></div><h4>Lorem ipsum dolor sitak ametn sit almet</h4><p>Lorem ipsum dolor sitak amet, co adipiscing elit, euismod poor.</p></div>
  <div class="news-item" style="top:2029px"><div class="date"><b>07</b><i>MAR</i></div><h4>Lorem ipsum dolor sitak ametn sit almet</h4><p>Lorem ipsum dolor sitak amet, co adipiscing elit, euismod poor.</p></div>

  <h3 class="abs heading col-title" style="left:865px;top:1815px"><span class="cap">O</span>ur catalogue</h3>
  <div class="ph" role="img" aria-label="Catalogue cover showing a glass automatic door entrance" style="left:865px;top:1883px;width:283px;height:200px;background:linear-gradient(135deg,#e6e6e6,#9a8c88)"></div>
  <div class="abs" style="left:865px;top:2020px;width:190px;height:40px;background:var(--red);color:#fff;font-family:'Mulish',sans-serif;font-style:italic;font-weight:700;font-size:13px;line-height:17px;padding:3px 0 0 78px">Download<br>Our catalogue</div>
  <div class="abs" style="left:872px;top:2014px;width:36px;height:44px;background:#fff;border:1px solid #ccc;font-size:10px;font-weight:700;color:var(--red);text-align:center;line-height:20px">PDF</div>
</section>

<footer class="abs footer">
  <h3 class="abs" style="left:52px;top:32px">Newsletter Signup</h3>
  <p class="abs footer-text" style="left:52px;top:66px;width:205px">Lorem ipsum dolor sit amet, consectetu er adipiscing elit, sed</p>
  <div class="f-input" style="left:52px;top:115px">Name</div>
  <div class="f-input" style="left:52px;top:158px">Email</div>
  <div class="abs" style="left:52px;top:207px;width:86px;height:28px;background:var(--red);color:#fff;font-size:13px;font-weight:700;text-align:center;line-height:28px">Subscribe</div>

  <div class="abs" style="left:348px;top:0;width:498px;height:297px;background:linear-gradient(#444,#2c2c2c)"></div>
  <h3 class="abs" style="left:413px;top:32px">Quick Links</h3>
  <ul class="abs links" style="left:413px;top:60px"><li>Home</li><li>Industrijska Vrata</li><li>Rolo Vrata</li><li>Kontrola Pristupa</li></ul>
  <ul class="abs links" style="left:555px;top:60px"><li>Reference</li><li>Contact</li></ul>
  <svg class="abs" style="left:678px;top:50px" width="80" height="70" viewBox="0 0 80 70"><circle cx="36" cy="34" r="28" fill="none" stroke="#888" stroke-width="4"/><path d="M64 30l6 8-10 0z" fill="#888"/><text x="36" y="40" text-anchor="middle" font-family="Lato,sans-serif" font-weight="700" font-size="17" fill="#999">24/7</text></svg>
  <div class="abs" style="left:408px;top:198px;width:345px;height:62px;background:#1c1c1c;border:1px solid #444;border-radius:6px"></div>
  <div class="abs" style="left:427px;top:218px;font-size:16px;color:var(--red)">CONTACT US</div>
  <svg class="abs" style="left:550px;top:213px" width="28" height="28" viewBox="0 0 28 28"><rect width="28" height="28" rx="4" fill="#555"/><path d="M9 6c-2 1-3 3-1 7s5 8 8 9c2 1 4 0 5-2l-3-3-2 2c-2-1-4-3-5-5l2-2z" fill="#ccc"/></svg>
  <div class="abs" style="left:598px;top:212px;font-size:23px;color:#fff">061/382-904</div>

  <h3 class="abs" style="left:913px;top:32px">Our Location</h3>
  <div class="ph" role="img" aria-label="Street map with location marker" style="left:910px;top:68px;width:238px;height:178px;background:linear-gradient(135deg,#e8ecd8,#c8d6c0);border:2px solid #fff"></div>
  <div class="abs" style="left:985px;top:105px;width:108px;height:70px;background:#fff;border-radius:4px;font-size:13px;line-height:18px;color:#333;padding:6px 8px">67 Lorem ipsum Street WA 6065, adipismg amet</div>
</footer>

<div class="abs bottom-bar">
  <div class="abs social" style="left:52px;top:21px;gap:8px" aria-label="Social links"><span style="width:22px;height:22px"></span><span style="width:22px;height:22px"></span><span style="width:22px;height:22px"></span></div>
  <div class="abs" style="left:0;top:23px;width:1200px;text-align:center;font-size:13px;color:#ccc">Copyright 2016 vortelan d.o.o. &nbsp;|&nbsp; All Rights Reserved</div>
  <div class="abs" style="right:52px;top:15px;font-family:'Mulish',sans-serif;font-weight:800;font-size:26px;color:#7a2a2e">vortelan d.o.o.</div>
</div>

</body>
</html>
```